Business Card for Jewelry Business

We need a new namecard design for a jewelry company based in Bangkok, Thailand. We have a new website recently and want the new namecard to reflect our new modern image. I have uploaded our old namecard to show you the information that needs to be on the namecard. Pls check our website www.qelburn.com for the new color scheme to help design the new namecard.

```html
<!DOCTYPE html>
<html lang="en">
<head>
<meta charset="utf-8">
<title>Qelburn Makers – Business Card</title>
<link rel="stylesheet" href="https://fonts.googleapis.com/css2?family=Libre+Baskerville:wght@400;700&display=swap">
<style>
  :root {
    --teal: #55c4c8;
    --ink: #161616;
    --paper: #ffffff;
    --backdrop: #e9eaec;
    --text-light: #f2f2f2;
  }
  html, body {
    margin: 0;
    width: 1200px;
    height: 801px;
    overflow: hidden;
    background: var(--backdrop);
    font-family: "Libre Baskerville", Georgia, serif;
  }
  .stage {
    position: relative;
    width: 1200px;
    height: 801px;
  }
  .card {
    position: absolute;
    top: 235px;
    width: 540px;
    height: 320px;
    border-radius: 16px;
    overflow: hidden;
    box-shadow: 0 10px 28px rgba(0,0,0,0.18);
  }
  .card--front {
    left: 40px;
    background: var(--teal);
  }
  .card--back {
    left: 620px;
    background: var(--ink);
  }
  .front-brand {
    position: absolute;
    left: 0; right: 0; top: 128px;
    text-align: center;
    color: var(--paper);
  }
  .front-brand__name {
    font-size: 40px;
    letter-spacing: 4px;
    line-height: 1;
  }
  .front-brand__sub {
    margin-top: 10px;
    font-size: 11px;
    letter-spacing: 3px;
  }
  .back-shape {
    position: absolute;
    inset: 0;
  }
  .back-brand {
    position: absolute;
    right: 44px;
    top: 92px;
    width: 150px;
    text-align: center;
    color: var(--teal);
    font-size: 22px;
    letter-spacing: 3px;
  }
  .social {
    position: absolute;
    right: 54px;
    top: 150px;
    display: flex;
    gap: 8px;
  }
  .social__dot {
    width: 22px;
    height: 22px;
    border-radius: 50%;
    background: var(--teal);
  }
  .details {
    position: absolute;
    left: 34px;
    top: 70px;
    color: var(--text-light);
  }
  .details__name {
    margin: 0;
    color: var(--teal);
    font-size: 25px;
    font-weight: 700;
    letter-spacing: 1px;
  }
  .details__role {
    margin: 4px 0 0;
    font-size: 11.5px;
  }
  .details__address {
    margin: 26px 0 0;
    font-size: 11.5px;
    line-height: 1.55;
    font-style: normal;
  }
  .contact {
    list-style: none;
    margin: 22px 0 0;
    padding: 0;
    font-size: 11.5px;
    line-height: 1.75;
  }
  .contact__item {
    display: flex;
    align-items: center;
    gap: 10px;
  }
  .contact__icon {
    width: 12px;
    height: 12px;
    fill: var(--teal);
    flex: none;
  }
</style>
</head>
<body>
<main class="stage">

  <section class="card card--front" aria-label="Card front">
    <div class="front-brand">
      <div class="front-brand__name">QELBURN</div>
      <div class="front-brand__sub">MAKERS</div>
    </div>
  </section>

  <section class="card card--back" aria-label="Card back">
    <svg class="back-shape" viewBox="0 0 540 320" width="540" height="320" aria-hidden="true">
      <path d="M300 0 C 300 140, 400 270, 540 300 L540 320 L540 0 Z" fill="var(--teal)"/>
      <path d="M316 0 C 318 130, 410 250, 540 276 L540 0 Z" fill="var(--paper)"/>
    </svg>

    <div class="back-brand">QELBURN</div>
    <div class="social" aria-hidden="true">
      <span class="social__dot"></span>
      <span class="social__dot"></span>
      <span class="social__dot"></span>
    </div>

    <div class="details">
      <h1 class="details__name">NIRA SANTHORN</h1>
      <p class="details__role">Sales &amp; Product Development Manager</p>
      <address class="details__address">
        128 Moo 7 Suanluang Road,<br>
        Prawet Industrial Park,<br>
        Bangkok, 10250 Thailand
      </address>
      <ul class="contact">
        <li class="contact__item">
          <svg class="contact__icon" viewBox="0 0 12 12"><path d="M2.5 1 L4.5 1 L5 3.5 L3.8 4.4 C4.5 6 6 7.5 7.6 8.2 L8.5 7 L11 7.5 L11 9.5 C11 10.3 10.3 11 9.5 11 C5 11 1 7 1 2.5 C1 1.7 1.7 1 2.5 1 Z"/></svg>
          +662-481-2207
        </li>
        <li class="contact__item">
          <svg class="contact__icon" viewBox="0 0 12 12"><rect x="1" y="4" width="10" height="7" rx="1"/><rect x="3" y="1" width="6" height="3"/></svg>
          +662-564-3190
        </li>
        <li class="contact__item">
          <svg class="contact__icon" viewBox="0 0 12 12"><path d="M1 2.5 H11 V9.5 H1 Z M1.5 3 L6 6.5 L10.5 3" stroke="var(--ink)" stroke-width="0.8"/></svg>
          nira@qelburn.com
        </li>
        <li class="contact__item">
          <svg class="contact__icon" viewBox="0 0 12 12"><circle cx="6" cy="6" r="5"/><path d="M1 6 H11 M6 1 C3.5 3.5 3.5 8.5 6 11 C8.5 8.5 8.5 3.5 6 1" fill="none" stroke="var(--ink)" stroke-width="0.7"/></svg>
          www.qelburn.com
        </li>
      </ul>
    </div>
  </section>

</main>
</body>
</html>
```